I need a full PowerPoint template (with multiple slide options) for a new imaging center company - Brightwell Medical Imaging. I have attached the Logo and Brand Identity here.

```html
<!DOCTYPE html>
<html lang="en">
<head>
<meta charset="utf-8">
<title>Brightwell Template – Dark Theme</title>
<link href="https://fonts.googleapis.com/css2?family=Montserrat:wght@400;500;600;700;800&display=swap" rel="stylesheet">
<style>
:root{
  --page:#ffffff;
  --ink:#2e2e38;
  --navy:#1b2452;
  --navy-deep:#141b40;
  --card:#253166;
  --card-light:#33418a;
  --line:#3a4790;
  --accent:#2f8fd8;
  --cyan:#4ec3e8;
  --pink:#e24d8f;
  --green:#3fc58a;
  --white:#ffffff;
  --muted:#a3acd6;
  --photo-a:#dbeaf5;
  --photo-b:#6f9fc8;
}
*{box-sizing:border-box;margin:0;padding:0}
html,body{width:802px;height:1200px;overflow:hidden;background:var(--page)}
.canvas{position:relative;width:802px;height:1200px;font-family:"Montserrat",sans-serif;background:var(--page)}
.doc-title{position:absolute;left:40px;top:26px;font-size:12px;font-weight:700;line-height:1.3;color:var(--ink);letter-spacing:.3px}
.grid{position:absolute;left:40px;top:70px;display:grid;grid-template-columns:repeat(4,175px);grid-auto-rows:96px;gap:5px 6px}
.slide{position:relative;background:var(--navy);overflow:hidden;color:var(--white);
  background-image:radial-gradient(rgba(255,255,255,.045) .6px,transparent .7px);background-size:5px 5px}
.slide > *{position:absolute}
.t{left:8px;top:7px;font-size:5px;font-weight:700;letter-spacing:.2px}
.sub{left:8px;top:14px;font-size:2.8px;color:var(--muted)}
.num{right:6px;top:5px;width:7px;height:7px;border-radius:50%;background:var(--white);color:var(--navy);font-size:3px;font-weight:700;display:flex;align-items:center;justify-content:center}
.big{font-size:7px;font-weight:800;line-height:1.15}
.brand{display:flex;align-items:center;gap:2px;font-size:5px;font-weight:700}
.brand .dot{width:5px;height:5px;border-radius:50%;background:var(--cyan)}
.p{font-size:3px;line-height:1.45;color:var(--muted)}
.h{font-size:3.6px;font-weight:700;color:var(--white);line-height:1.2}
.ph{background:linear-gradient(135deg,var(--photo-a),var(--photo-b))}
.box{background:var(--card);border-radius:2px}
.box-light{background:var(--card-light);border-radius:2px}
.stat{font-size:6px;font-weight:800;color:var(--cyan)}
.list{display:flex;flex-direction:column;gap:4px}
.row{display:flex;align-items:center;gap:3px;font-size:3px;color:var(--muted)}
.row i{display:flex;align-items:center;justify-content:center;width:6px;height:6px;border-radius:50%;background:var(--accent);flex:none;font-style:normal;color:#fff;font-size:2.6px;font-weight:700}
.bar{height:2px;border-radius:1px;background:var(--line)}
.pill{font-size:2.8px;font-weight:700;background:var(--accent);color:#fff;border-radius:3px;padding:1.2px 3px}
</style>
</head>
<body>
<div class="canvas">
  <div class="doc-title">BRIGHTWELL TEMPLATE<br>DARK THEME</div>

  <div class="grid">
    <!-- Row 1 : covers + agenda -->
    <div class="slide">
      <div class="brand" style="left:10px;top:14px"><span class="dot"></span>Brightwell</div>
      <div class="big" style="left:10px;top:36px">PRESENTATION<br>TITLE GOES<br>HERE</div>
      <div class="p" style="left:10px;top:64px;width:70px">Subtitle or presenter name goes here</div>
      <div class="ph" style="right:-16px;top:10px;width:78px;height:78px;border-radius:50%" role="img" aria-label="Imaging scan photo"></div>
    </div>
    <div class="slide">
      <div class="ph" style="left:0;top:0;width:80px;height:96px" role="img" aria-label="Doctor reviewing a scan"></div>
      <div class="brand" style="left:88px;top:16px"><span class="dot"></span>Brightwell</div>
      <div class="big" style="left:88px;top:36px">PRESENTATION<br>TITLE GOES<br>HERE</div>
      <div class="p" style="left:88px;top:64px;width:76px">Subtitle or presenter name goes here</div>
    </div>
    <div class="slide">
      <div class="brand" style="left:10px;top:14px"><span class="dot"></span>Brightwell</div>
      <div class="big" style="left:10px;top:36px">PRESENTATION<br>TITLE GOES<br>HERE</div>
      <div class="p" style="left:10px;top:64px;width:70px">Subtitle or presenter name goes here</div>
      <div class="ph" style="right:0;top:0;width:78px;height:96px;border-radius:40px 0 0 40px" role="img" aria-label="Patient in scanner"></div>
    </div>
    <div class="slide">
      <div class="t">PRESENTATION AGENDA</div><div class="num">4</div>
      <svg style="left:12px;top:24px" width="54" height="54" viewBox="0 0 54 54"><circle cx="27" cy="27" r="20" fill="none" stroke="var(--card-light)" stroke-width="8"/><circle cx="27" cy="27" r="20" fill="none" stroke="var(--cyan)" stroke-width="8" stroke-dasharray="80 126" transform="rotate(-90 27 27)"/><text x="27" y="29" text-anchor="middle" font-size="6" font-weight="800" fill="#fff" font-family="Montserrat,sans-serif">65%</text></svg>
      <div class="list" style="left:76px;top:22px;gap:3.5px">
        <div class="row"><i>1</i>Introduction and welcome</div>
        <div class="row"><i>2</i>About our imaging centre</div>
        <div class="row"><i>3</i>Services and equipment</div>
        <div class="row"><i>4</i>Our medical team</div>
        <div class="row"><i>5</i>Results and next steps</div>
        <div class="row"><i>6</i>Questions and contact</div>
      </div>
    </div>

    <!-- Row 2 -->
    <div class="slide">
      <div class="t">TITLE GOES HERE</div><div class="num">5</div>
      <div class="box" style="left:8px;top:22px;width:50px;height:66px"></div>
      <div class="box" style="left:62.5px;top:22px;width:50px;height:66px"></div>
      <div class="box" style="left:117px;top:22px;width:50px;height:66px"></div>
      <svg style="left:8px;top:22px" width="159" height="30" viewBox="0 0 159 30"><g fill="var(--cyan)"><circle cx="25" cy="12" r="6"/><circle cx="79.5" cy="12" r="6"/><circle cx="134" cy="12" r="6"/></g><g stroke="var(--navy)" stroke-width="1.2" fill="none"><path d="M22 12h6M25 9v6"/><path d="M76.5 12l2 2 3.5-4"/><circle cx="134" cy="12" r="2.5"/></g></svg>
      <div class="h" style="left:12px;top:40px">MRI Scans</div><div class="p" style="left:12px;top:46px;width:42px">Detailed images of soft tissue and organs.</div>
      <div class="h" style="left:66.5px;top:40px">CT Scans</div><div class="p" style="left:66.5px;top:46px;width:42px">Fast cross-section views for clear results.</div>
      <div class="h" style="left:121px;top:40px">Ultrasound</div><div class="p" style="left:121px;top:46px;width:42px">Safe live imaging with no radiation used.</div>
    </div>
    <div class="slide">
      <div class="t" style="left:0;width:175px;text-align:center;top:14px">TEXT PARAGRAPH</div><div class="num">6</div>
      <div class="p" style="left:20px;top:24px;width:135px;text-align:center">Write a short paragraph about the imaging centre, its services and its care for each patient. Our team brings modern equipment and kind, expert staff together to give fast and accurate results for every referral we receive.</div>
      <div class="p" style="left:20px;top:50px;width:135px;text-align:center">Add a second paragraph here to share more about the mission, values and the way the centre works with local doctors and clinics across the region.</div>
      <div class="pill" style="left:74px;top:76px">Read More</div>
    </div>
    <div class="slide">
      <div class="t">TITLE GOES HERE</div><div class="num">7</div>
      <div class="ph" style="left:8px;top:20px;width:68px;height:68px" role="img" aria-label="Clinic photo"></div>
      <div class="p" style="left:82px;top:20px;width:85px">Add a short description of the topic on this slide with one or two lines.</div>
      <div class="box" style="left:82px;top:36px;width:85px;height:24px"></div>
      <div class="h" style="left:86px;top:40px">Modern Equipment</div><div class="p" style="left:86px;top:46px;width:78px">Latest scanners for sharp images.</div>
      <div class="box" style="left:82px;top:63px;width:85px;height:25px"></div>
      <div class="h" style="left:86px;top:67px">Expert Team</div><div class="p" style="left:86px;top:73px;width:78px">Skilled staff and radiologists.</div>
    </div>
    <div class="slide">
      <div class="t">TITLE GOES HERE</div><div class="num">8</div>
      <div class="ph" style="left:8px;top:18px;width:159px;height:32px" role="img" aria-label="Scan room photo"></div>
      <div class="box" style="left:8px;top:54px;width:50px;height:34px"></div>
      <div class="box" style="left:62.5px;top:54px;width:50px;height:34px"></div>
      <div class="box" style="left:117px;top:54px;width:50px;height:34px"></div>
      <div class="stat" style="left:12px;top:57px;font-size:5px">01</div><div class="p" style="left:12px;top:65px;width:43px">Book your scan online or by phone.</div>
      <div class="stat" style="left:66.5px;top:57px;font-size:5px">02</div><div class="p" style="left:66.5px;top:65px;width:43px">Visit the centre for a quick exam.</div>
      <div class="stat" style="left:121px;top:57px;font-size:5px">03</div><div class="p" style="left:121px;top:65px;width:43px">Get results sent to your doctor.</div>
    </div>

    <!-- Row 3 -->
    <div class="slide">
      <div class="t">TITLE GOES HERE</div><div class="num">9</div>
      <div class="ph" style="left:12px;top:22px;width:60px;height:60px;border-radius:50%" role="img" aria-label="Equipment photo"></div>
      <div class="list" style="left:80px;top:22px;gap:2.5px">
        <div class="h">Service point one</div><div class="p" style="width:85px">Short line about this service here.</div>
        <div class="h">Service point two</div><div class="p" style="width:85px">Short line about this service here.</div>
        <div class="h">Service point three</div><div class="p" style="width:85px">Short line about this service here.</div>
        <div class="h">Service point four</div><div class="p" style="width:85px">Short line about this service here.</div>
      </div>
    </div>
    <div class="slide">
      <div class="t">TITLE GOES HERE</div><div class="num">10</div>
      <div class="ph" style="left:8px;top:20px;width:49px;height:32px" role="img" aria-label="Staff photo"></div>
      <div class="ph" style="left:63px;top:20px;width:49px;height:32px" role="img" aria-label="Scanner photo"></div>
      <div class="ph" style="left:118px;top:20px;width:49px;height:32px" role="img" aria-label="Reception photo"></div>
      <div class="h" style="left:8px;top:56px">Our Staff</div><div class="p" style="left:8px;top:62px;width:49px">Caring people who guide each patient.</div>
      <div class="h" style="left:63px;top:56px">Our Scanners</div><div class="p" style="left:63px;top:62px;width:49px">New machines with low dose settings.</div>
      <div class="h" style="left:118px;top:56px">Our Centre</div><div class="p" style="left:118px;top:62px;width:49px">Calm rooms and easy free parking.</div>
    </div>
    <div class="slide">
      <div class="t">TITLE GOES HERE</div><div class="num">11</div>
      <div class="box-light" style="left:8px;top:20px;width:49px;height:68px"></div>
      <div class="box-light" style="left:63px;top:20px;width:49px;height:68px"></div>
      <div class="box-light" style="left:118px;top:20px;width:49px;height:68px"></div>
      <div class="stat" style="left:13px;top:25px">01</div><div class="h" style="left:13px;top:35px">Referral</div><div class="p" style="left:13px;top:41px;width:40px">Your doctor sends the request to our team.</div>
      <div class="stat" style="left:68px;top:25px">02</div><div class="h" style="left:68px;top:35px">Scan Day</div><div class="p" style="left:68px;top:41px;width:40px">A short visit with a friendly technologist.</div>
      <div class="stat" style="left:123px;top:25px">03</div><div class="h" style="left:123px;top:35px">Report</div><div class="p" style="left:123px;top:41px;width:40px">A radiologist reviews and shares results.</div>
    </div>
    <div class="slide">
      <div class="t">TITLE GOES HERE</div><div class="num">12</div>
      <svg style="left:8px;top:24px" width="159" height="60" viewBox="0 0 159 60">
        <g fill="var(--accent)"><circle cx="8" cy="10" r="7"/><circle cx="8" cy="42" r="7"/><circle cx="87" cy="10" r="7"/><circle cx="87" cy="42" r="7"/></g>
        <g stroke="#fff" stroke-width="1.4" fill="none"><path d="M4.5 10l2.5 2.5 4.5-5"/><path d="M4.5 42l2.5 2.5 4.5-5"/><path d="M83.5 10l2.5 2.5 4.5-5"/><path d="M83.5 42l2.5 2.5 4.5-5"/></g>
      </svg>
      <div class="h" style="left:28px;top:26px">Fast Booking</div><div class="p" style="left:28px;top:32px;width:54px">Same week slots for most scans.</div>
      <div class="h" style="left:28px;top:58px">Clear Reports</div><div class="p" style="left:28px;top:64px;width:54px">Plain notes for you and your doctor.</div>
      <div class="h" style="left:107px;top:26px">Low Dose</div><div class="p" style="left:107px;top:32px;width:58px">Safe settings on every machine.</div>
      <div class="h" style="left:107px;top:58px">Open Late</div><div class="p" style="left:107px;top:64px;width:58px">Evening and weekend hours.</div>
    </div>

    <!-- Row 4 -->
    <div class="slide">
      <div class="t">TITLE GOES HERE</div><div class="num">13</div>
      <div class="box" style="left:8px;top:20px;width:159px;height:15px"></div>
      <div class="box" style="left:8px;top:38px;width:159px;height:15px"></div>
      <div class="box" style="left:8px;top:56px;width:159px;height:15px"></div>
      <div class="box" style="left:8px;top:74px;width:159px;height:15px"></div>
      <div class="row" style="left:12px;top:24.5px"><i>1</i><b style="color:#fff">Step one</b>&nbsp;– Add a short line of text here.</div>
      <div class="row" style="left:12px;top:42.5px"><i>2</i><b style="color:#fff">Step two</b>&nbsp;– Add a short line of text here.</div>
      <div class="row" style="left:12px;top:60.5px"><i>3</i><b style="color:#fff">Step three</b>&nbsp;– Add a short line of text here.</div>
      <div class="row" style="left:12px;top:78.5px"><i>4</i><b style="color:#fff">Step four</b>&nbsp;– Add a short line of text here.</div>
    </div>
    <div class="slide">
      <div class="t">TITLE GOES HERE</div><div class="num">14</div>
      <div class="box-light" style="left:8px;top:20px;width:77px;height:32px"></div>
      <div class="box-light" style="left:90px;top:20px;width:77px;height:32px"></div>
      <div class="box-light" style="left:8px;top:56px;width:77px;height:32px"></div>
      <div class="box-light" style="left:90px;top:56px;width:77px;height:32px"></div>
      <div class="h" style="left:13px;top:25px">X-Ray</div><div class="p" style="left:13px;top:31px;width:68px">Quick walk-in images of bones and chest.</div>
      <div class="h" style="left:95px;top:25px">Mammography</div><div class="p" style="left:95px;top:31px;width:68px">Gentle 3D breast screening each year.</div>
      <div class="h" style="left:13px;top:61px">Bone Density</div><div class="p" style="left:13px;top:67px;width:68px">Simple test to check bone strength.</div>
      <div class="h" style="left:95px;top:61px">PET Scan</div><div class="p" style="left:95px;top:67px;width:68px">Shows how organs and tissue work.</div>
    </div>
    <div class="slide">
      <div class="t">TEAM MEMBER</div><div class="num">15</div>
      <div class="ph" style="left:18px;top:22px;width:54px;height:54px;border-radius:50%" role="img" aria-label="Team member portrait"></div>
      <div class="h" style="left:82px;top:26px;font-size:4.2px">Member Name</div>
      <div class="p" style="left:82px;top:32px;color:var(--cyan)">Lead Radiologist</div>
      <div class="p" style="left:82px;top:40px;width:84px">Add a short bio for this team member here. Share their training, focus area and years of care.</div>
      <div class="bar" style="left:82px;top:62px;width:84px"></div><div class="bar" style="left:82px;top:62px;width:64px;background:var(--cyan)"></div>
      <div class="bar" style="left:82px;top:68px;width:84px"></div><div class="bar" style="left:82px;top:68px;width:50px;background:var(--cyan)"></div>
    </div>
    <div class="slide">
      <div class="t">TEAM MEMBERS</div><div class="num">16</div>
      <div class="ph" style="left:28px;top:22px;width:42px;height:42px;border-radius:50%" role="img" aria-label="Team member portrait"></div>
      <div class="ph" style="left:105px;top:22px;width:42px;height:42px;border-radius:50%" role="img" aria-label="Team member portrait"></div>
      <div class="h" style="left:10px;top:68px;width:78px;text-align:center">Name Here</div>
      <div class="p" style="left:10px;top:74px;width:78px;text-align:center">Imaging Technologist</div>
      <div class="h" style="left:87px;top:68px;width:78px;text-align:center">Name Here</div>
      <div class="p" style="left:87px;top:74px;width:78px;text-align:center">Patient Care Nurse</div>
    </div>

    <!-- Row 5 -->
    <div class="slide">
      <div class="t">TITLE GOES HERE</div><div class="num">17</div>
      <svg style="left:14px;top:30px" width="30" height="30" viewBox="0 0 30 30"><circle cx="15" cy="15" r="14" fill="var(--cyan)"/><path d="M9 15h12M15 9v12" stroke="var(--navy)" stroke-width="2.4"/></svg>
      <div class="h" style="left:52px;top:28px;font-size:4.2px">Care That Comes First</div>
      <div class="p" style="left:52px;top:35px;width:112px">Add a clear point about the service here with a short line of text. Explain why it matters to each patient and how the team makes it easy.</div>
      <div class="pill" style="left:52px;top:58px">Learn More</div>
    </div>
    <div class="slide">
      <div class="t">GRID SLIDE</div><div class="num">18</div>
      <div class="box" style="left:8px;top:20px;width:38px;height:33px"></div>
      <div class="box" style="left:48px;top:20px;width:38px;height:33px"></div>
      <div class="box" style="left:88px;top:20px;width:38px;height:33px"></div>
      <div class="box" style="left:128px;top:20px;width:39px;height:33px"></div>
      <div class="box" style="left:8px;top:55px;width:38px;height:33px"></div>
      <div class="box" style="left:48px;top:55px;width:38px;height:33px"></div>
      <div class="box" style="left:88px;top:55px;width:38px;height:33px"></div>
      <div class="box" style="left:128px;top:55px;width:39px;height:33px"></div>
      <div class="h" style="left:11px;top:24px">MRI</div><div class="p" style="left:11px;top:30px;width:33px">Short text for this tile.</div>
      <div class="h" style="left:51px;top:24px">CT</div><div class="p" style="left:51px;top:30px;width:33px">Short text for this tile.</div>
      <div class="h" style="left:91px;top:24px">X-Ray</div><div class="p" style="left:91px;top:30px;width:33px">Short text for this tile.</div>
      <div class="h" style="left:131px;top:24px">PET</div><div class="p" style="left:131px;top:30px;width:33px">Short text for this tile.</div>
      <div class="h" style="left:11px;top:59px">Ultrasound</div><div class="p" style="left:11px;top:65px;width:33px">Short text for this tile.</div>
      <div class="h" style="left:51px;top:59px">Dexa</div><div class="p" style="left:51px;top:65px;width:33px">Short text for this tile.</div>
      <div class="h" style="left:91px;top:59px">Fluoro</div><div class="p" style="left:91px;top:65px;width:33px">Short text for this tile.</div>
      <div class="h" style="left:131px;top:59px">Mammo</div><div class="p" style="left:131px;top:65px;width:33px">Short text for this tile.</div>
    </div>
    <div class="slide">
      <div class="t">TITLE GOES HERE</div><div class="num">19</div>
      <svg style="left:8px;top:24px" width="159" height="30" viewBox="0 0 159 30"><line x1="30" y1="12" x2="130" y2="12" stroke="var(--line)" stroke-width="1" stroke-dasharray="2 2"/><g fill="var(--accent)"><circle cx="26" cy="12" r="11"/><circle cx="79.5" cy="12" r="11"/><circle cx="133" cy="12" r="11"/></g><g stroke="#fff" stroke-width="1.4" fill="none"><rect x="21" y="8" width="10" height="8" rx="1"/><circle cx="79.5" cy="12" r="4"/><path d="M128 12l3.5 3.5 6-7"/></g></svg>
      <div class="h" style="left:8px;top:56px;width:52px;text-align:center">Step One</div><div class="p" style="left:8px;top:62px;width:52px;text-align:center">Book a time that works for you.</div>
      <div class="h" style="left:61.5px;top:56px;width:52px;text-align:center">Step Two</div><div class="p" style="left:61.5px;top:62px;width:52px;text-align:center">Have your scan with our team.</div>
      <div class="h" style="left:115px;top:56px;width:52px;text-align:center">Step Three</div><div class="p" style="left:115px;top:62px;width:52px;text-align:center">Receive your report quickly.</div>
    </div>
    <div class="slide">
      <div class="num">20</div>
      <div class="stat" style="left:0;width:175px;text-align:center;top:14px;font-size:16px;line-height:1">“</div>
      <div class="p" style="left:22px;top:34px;width:131px;text-align:center;font-size:3.4px;color:#dfe4f7">A short quote from a patient or doctor goes here. The staff were kind, the scan was quick and the results reached my doctor the very next day.</div>
      <div class="ph" style="left:80px;top:58px;width:15px;height:15px;border-radius:50%" role="img" aria-label="Quote author portrait"></div>
      <div class="h" style="left:0;width:175px;text-align:center;top:76px">Quote Author</div>
      <div class="p" style="left:0;width:175px;text-align:center;top:81px">Patient</div>
    </div>

    <!-- Row 6 -->
    <div class="slide">
      <div class="t">TITLE GOES HERE</div><div class="num">21</div>
      <svg style="left:12px;top:28px" width="36" height="36" viewBox="0 0 36 36"><circle cx="18" cy="18" r="17" fill="var(--accent)"/><circle cx="18" cy="18" r="7" fill="none" stroke="#fff" stroke-width="3" stroke-dasharray="4 2"/></svg>
      <div class="h" style="left:56px;top:26px;font-size:4.2px">Our Process</div>
      <div class="p" style="left:56px;top:33px;width:108px">Add a short process note here for this slide. Describe how each scan is planned, done and checked by our team.</div>
      <div class="row" style="left:56px;top:54px"><i></i>Planned with your doctor</div>
      <div class="row" style="left:56px;top:62px"><i></i>Checked by a radiologist</div>
      <div class="row" style="left:56px;top:70px"><i></i>Shared within one day</div>
    </div>
    <div class="slide">
      <div class="t">TITLE GOES HERE</div><div class="num">22</div>
      <div class="box" style="left:8px;top:20px;width:159px;height:11px;background:var(--accent)"></div>
      <div class="box" style="left:8px;top:34px;width:159px;height:11px"></div>
      <div class="box" style="left:8px;top:48px;width:159px;height:11px"></div>
      <div class="box" style="left:8px;top:62px;width:159px;height:11px"></div>
      <div class="box" style="left:8px;top:76px;width:159px;height:11px"></div>
      <div class="h" style="left:12px;top:23.5px">Service</div><div class="h" style="left:80px;top:23.5px">Time</div><div class="h" style="left:130px;top:23.5px">Report</div>
      <div class="p" style="left:12px;top:37px">MRI Scan</div><div class="p" style="left:80px;top:37px">45 min</div><div class="p" style="left:130px;top:37px">24 hours</div>
      <div class="p" style="left:12px;top:51px">CT Scan</div><div class="p" style="left:80px;top:51px">15 min</div><div class="p" style="left:130px;top:51px">24 hours</div>
      <div class="p" style="left:12px;top:65px">Ultrasound</div><div class="p" style="left:80px;top:65px">30 min</div><div class="p" style="left:130px;top:65px">Same day</div>
      <div class="p" style="left:12px;top:79px">X-Ray</div><div class="p" style="left:80px;top:79px">10 min</div><div class="p" style="left:130px;top:79px">Same day</div>
    </div>
    <div class="slide">
      <div class="big" style="left:14px;top:34px;font-size:8px">THANK<br>YOU</div>
      <div class="p" style="left:14px;top:56px;width:70px">Thank you for your time and attention.</div>
      <div class="ph" style="right:8px;top:16px;width:64px;height:64px;border-radius:50%" role="img" aria-label="Clinic photo"></div>
    </div>
    <div class="slide" style="background-color:var(--navy-deep)">
      <div style="left:24px;top:24px;width:48px;height:48px;border-radius:50%;background:linear-gradient(135deg,var(--cyan),var(--accent))"></div>
      <div style="left:38px;top:38px;width:20px;height:20px;border-radius:50%;background:var(--navy-deep)"></div>
      <div class="big" style="left:86px;top:36px;font-size:8px">BREAK<br><span style="color:var(--cyan)">SLIDE</span></div>
      <div class="p" style="left:86px;top:56px;width:76px">Section two starts here</div>
    </div>

    <!-- Row 7 -->
    <div class="slide">
      <div class="t">TITLE GOES HERE</div><div class="num">25</div>
      <div class="ph" style="left:8px;top:20px;width:76px;height:52px" role="img" aria-label="Imaging room photo"></div>
      <div class="ph" style="left:90px;top:20px;width:77px;height:24px" role="img" aria-label="Scan image photo"></div>
      <div class="ph" style="left:90px;top:48px;width:77px;height:24px" role="img" aria-label="Doctor photo"></div>
      <div class="p" style="left:8px;top:76px;width:159px">Add a short caption for this photo gallery to tell the story of the centre.</div>
    </div>
    <div class="slide">
      <div class="t">DEVICE SLIDE</div><div class="num">26</div>
      <div class="box-light" style="left:64px;top:22px;width:100px;height:58px"></div>
      <div class="ph" style="left:68px;top:26px;width:92px;height:50px" role="img" aria-label="Screen preview"></div>
      <div class="box-light" style="left:100px;top:80px;width:28px;height:4px"></div>
      <div class="h" style="left:8px;top:26px">Online Portal</div>
      <div class="p" style="left:8px;top:32px;width:52px">Patients view reports and book scans from home.</div>
      <div class="row" style="left:8px;top:52px"><i></i>View reports</div>
      <div class="row" style="left:8px;top:60px"><i></i>Book scans</div>
      <div class="row" style="left:8px;top:68px"><i></i>Share images</div>
    </div>
    <div class="slide">
      <div class="t">TITLE GOES HERE</div><div class="num">27</div>
      <div style="left:26px;top:22px;width:122px;height:60px;background:linear-gradient(135deg,var(--card-light),var(--accent));transform:skewX(-12deg)" role="img" aria-label="Location area"></div>
      <svg style="left:80px;top:34px" width="14" height="20" viewBox="0 0 14 20"><path d="M7 19s6-7 6-11a6 6 0 0 0-12 0c0 4 6 11 6 11z" fill="var(--pink)"/><circle cx="7" cy="8" r="2.2" fill="#fff"/></svg>
      <div class="p" style="left:8px;top:86px">Main centre · add your address line here</div>
    </div>
    <div class="slide">
      <div class="t">PRICING TABLE</div><div class="num">28</div>
      <svg style="left:8px;top:20px" width="159" height="68" viewBox="0 0 159 68">
        <rect width="159" height="11" fill="var(--accent)"/>
        <g fill="var(--card)"><rect y="14" width="159" height="11"/><rect y="28" width="159" height="11"/><rect y="42" width="159" height="11"/><rect y="56" width="159" height="11"/></g>
        <g stroke="var(--navy)" stroke-width="1"><line x1="53" y1="0" x2="53" y2="68"/><line x1="106" y1="0" x2="106" y2="68"/></g>
        <g font-family="Montserrat,sans-serif" font-size="3.2" fill="#fff" font-weight="700"><text x="4" y="7">Plan</text><text x="57" y="7">Basic</text><text x="110" y="7">Premium</text></g>
        <g font-family="Montserrat,sans-serif" font-size="3" fill="var(--muted)"><text x="4" y="21">Scan type</text><text x="57" y="21">X-Ray</text><text x="110" y="21">MRI + CT</text><text x="4" y="35">Report time</text><text x="57" y="35">48 hours</text><text x="110" y="35">24 hours</text><text x="4" y="49">Follow up</text><text x="57" y="49">Phone</text><text x="110" y="49">In person</text><text x="4" y="63">Price</text><text x="57" y="63">$99</text><text x="110" y="63">$249</text></g>
      </svg>
    </div>

    <!-- Row 8 -->
    <div class="slide">
      <div class="t">BAR CHART</div><div class="num">29</div>
      <svg style="left:44px;top:22px" width="125" height="66" viewBox="0 0 125 66">
        <g stroke="var(--line)" stroke-width=".4"><line x1="0" y1="10" x2="125" y2="10"/><line x1="0" y1="30" x2="125" y2="30"/><line x1="0" y1="50" x2="125" y2="50"/></g>
        <g fill="var(--cyan)"><rect x="4" y="28" width="8" height="30"/><rect x="24" y="16" width="8" height="42"/><rect x="44" y="34" width="8" height="24"/><rect x="64" y="8" width="8" height="50"/><rect x="84" y="22" width="8" height="36"/><rect x="104" y="4" width="8" height="54"/></g>
        <g fill="var(--accent)"><rect x="13" y="38" width="6" height="20"/><rect x="33" y="28" width="6" height="30"/><rect x="53" y="42" width="6" height="16"/><rect x="73" y="24" width="6" height="34"/><rect x="93" y="32" width="6" height="26"/><rect x="113" y="18" width="6" height="40"/></g>
        <g font-family="Montserrat,sans-serif" font-size="3" fill="var(--muted)"><text x="4" y="64">Jan</text><text x="24" y="64">Feb</text><text x="44" y="64">Mar</text><text x="64" y="64">Apr</text><text x="84" y="64">May</text><text x="104" y="64">Jun</text></g>
      </svg>
      <div class="stat" style="left:8px;top:24px">75%</div><div class="p" style="left:8px;top:32px">MRI visits</div>
      <div class="stat" style="left:8px;top:44px;color:var(--accent)">40%</div><div class="p" style="left:8px;top:52px">CT visits</div>
    </div>
    <div class="slide">
      <div class="t">PIE CHART</div><div class="num">30</div>
      <svg style="left:12px;top:20px" width="66" height="66" viewBox="0 0 66 66">
        <circle cx="33" cy="33" r="16" fill="none" stroke="var(--pink)" stroke-width="32" stroke-dasharray="40 101" transform="rotate(-90 33 33)"/>
        <circle cx="33" cy="33" r="16" fill="none" stroke="var(--cyan)" stroke-width="32" stroke-dasharray="35 101" stroke-dashoffset="-40" transform="rotate(-90 33 33)"/>
        <circle cx="33" cy="33" r="16" fill="none" stroke="var(--accent)" stroke-width="32" stroke-dasharray="26 101" stroke-dashoffset="-75" transform="rotate(-90 33 33)"/>
      </svg>
      <div class="list" style="left:90px;top:24px;gap:3px">
        <div class="row"><i style="background:var(--pink)"></i><b style="color:#fff">40%</b> MRI scans</div><div class="p" style="width:74px">Most booked service</div>
        <div class="row"><i style="background:var(--cyan)"></i><b style="color:#fff">35%</b> CT scans</div><div class="p" style="width:74px">Fast growing service</div>
        <div class="row"><i></i><b style="color:#fff">25%</b> Ultrasound</div><div class="p" style="width:74px">Steady each month</div>
      </div>
    </div>
    <div class="slide">
      <div class="t">COMPARISON SLIDE</div><div class="num">31</div>
      <div class="box" style="left:8px;top:20px;width:77px;height:68px"></div>
      <div class="box" style="left:90px;top:20px;width:77px;height:68px"></div>
      <div class="h" style="left:13px;top:25px;color:var(--cyan)">Option A</div>
      <div class="h" style="left:95px;top:25px;color:var(--pink)">Option B</div>
      <div class="list" style="left:13px;top:34px;gap:3px">
        <div class="row"><i></i>Lower cost</div><div class="row"><i></i>Walk-in slots</div><div class="row"><i></i>Basic report</div><div class="row"><i></i>Two day results</div>
      </div>
      <div class="list" style="left:95px;top:34px;gap:3px">
        <div class="row"><i style="background:var(--pink)"></i>Full service</div><div class="row"><i style="background:var(--pink)"></i>Fixed times</div><div class="row"><i style="background:var(--pink)"></i>Detailed report</div><div class="row"><i style="background:var(--pink)"></i>Next day results</div>
      </div>
    </div>
    <div class="slide">
      <div class="t">CLIENT TESTIMONIALS</div><div class="num">32</div>
      <div class="box" style="left:8px;top:20px;width:159px;height:32px"></div>
      <div class="box" style="left:8px;top:56px;width:159px;height:32px"></div>
      <div class="ph" style="left:13px;top:26px;width:19px;height:19px;border-radius:50%" role="img" aria-label="Client portrait"></div>
      <div class="ph" style="left:13px;top:62px;width:19px;height:19px;border-radius:50%" role="img" aria-label="Client portrait"></div>
      <div class="h" style="left:38px;top:25px">Client Name</div><div class="p" style="left:38px;top:31px;width:124px">Short client review text here. The visit was calm, quick and the team explained every step.</div>
      <div class="h" style="left:38px;top:61px">Client Name</div><div class="p" style="left:38px;top:67px;width:124px">Short client review text here. Booking was easy and my results came back the next day.</div>
    </div>

    <!-- Row 9 -->
    <div class="slide">
      <div class="num">33</div>
      <div class="big" style="left:10px;top:14px;font-size:6px">TITLE GOES<br>HERE WITH<br>BIG BOLD<br>TEXT</div>
      <div class="p" style="left:10px;top:50px;width:72px">Add a short summary line to support the main heading on this slide.</div>
      <div class="stat" style="left:96px;top:20px">98%</div><div class="p" style="left:96px;top:28px;width:70px">Patient satisfaction</div>
      <div class="stat" style="left:96px;top:40px">12k</div><div class="p" style="left:96px;top:48px;width:70px">Scans each year</div>
      <div class="stat" style="left:96px;top:60px">24h</div><div class="p" style="left:96px;top:68px;width:70px">Average report time</div>
    </div>
    <div class="slide">
      <div class="t">TIMELINE SLIDE</div><div class="num">34</div>
      <svg style="left:8px;top:38px" width="159" height="20" viewBox="0 0 159 20"><line x1="0" y1="10" x2="159" y2="10" stroke="var(--line)" stroke-width="2"/><g fill="var(--cyan)"><circle cx="20" cy="10" r="5"/><circle cx="60" cy="10" r="5"/><circle cx="100" cy="10" r="5"/><circle cx="140" cy="10" r="5"/></g></svg>
      <div class="p" style="left:8px;top:22px;width:40px;text-align:center">Centre opens</div>
      <div class="p" style="left:88px;top:22px;width:40px;text-align:center">MRI wing added</div>
      <div class="h" style="left:8px;top:62px;width:40px;text-align:center">2021</div><div class="h" style="left:48px;top:62px;width:40px;text-align:center">2022</div><div class="h" style="left:88px;top:62px;width:40px;text-align:center">2023</div><div class="h" style="left:128px;top:62px;width:40px;text-align:center">2024</div>
      <div class="p" style="left:48px;top:68px;width:40px;text-align:center">New CT unit</div>
      <div class="p" style="left:128px;top:68px;width:40px;text-align:center">Second site</div>
    </div>
    <div class="slide">
      <div class="num">35</div>
      <div class="big" style="left:18px;top:28px;width:139px;text-align:center;font-size:6px">ONE SHORT STATEMENT TO SHARE WITH THE AUDIENCE</div>
      <div class="p" style="left:25px;top:48px;width:125px;text-align:center">Add a supporting line of text here to give more context to the main statement.</div>
    </div>
    <div class="slide">
      <div class="num">36</div>
      <div class="big" style="left:18px;top:28px;width:139px;text-align:center;font-size:6px">ONE SHORT STATEMENT TO SHARE WITH THE AUDIENCE</div>
      <div class="p" style="left:25px;top:48px;width:125px;text-align:center">Add a supporting line of text here to give more context to the main statement.</div>
    </div>

    <!-- Row 10 -->
    <div class="slide">
      <div class="t">SELECT YOUR PLAN</div><div class="num">37</div>
      <div class="p" style="left:8px;top:15px">Add a short note about plans.</div>
      <div class="box" style="left:8px;top:24px;width:50px;height:64px"></div>
      <div class="box-light" style="left:62.5px;top:24px;width:50px;height:64px"></div>
      <div class="box" style="left:117px;top:24px;width:50px;height:64px"></div>
      <div class="h" style="left:8px;top:28px;width:50px;text-align:center">Basic</div><div class="stat" style="left:8px;top:34px;width:50px;text-align:center">$99</div>
      <div class="p" style="left:12px;top:44px;width:42px;text-align:center">X-Ray and one report by post.</div>
      <div class="pill" style="left:21px;top:76px">Choose</div>
      <div class="h" style="left:62.5px;top:28px;width:50px;text-align:center">Standard</div><div class="stat" style="left:62.5px;top:34px;width:50px;text-align:center">$179</div>
      <div class="p" style="left:66.5px;top:44px;width:42px;text-align:center">CT scan with online report.</div>
      <div class="pill" style="left:75.5px;top:76px">Choose</div>
      <div class="h" style="left:117px;top:28px;width:50px;text-align:center">Premium</div><div class="stat" style="left:117px;top:34px;width:50px;text-align:center">$249</div>
      <div class="p" style="left:121px;top:44px;width:42px;text-align:center">MRI, CT and a follow up visit.</div>
      <div class="pill" style="left:130px;top:76px">Choose</div>
    </div>
    <div class="slide">
      <div class="t">DASHBOARD</div><div class="num">38</div>
      <svg style="left:8px;top:20px" width="159" height="70" viewBox="0 0 159 70">
        <g stroke="var(--line)" stroke-width=".4"><line x1="0" y1="12" x2="159" y2="12"/><line x1="0" y1="32" x2="159" y2="32"/><line x1="0" y1="52" x2="159" y2="52"/></g>
        <g fill="var(--accent)"><rect x="6" y="30" width="10" height="32"/><rect x="26" y="20" width="10" height="42"/><rect x="46" y="38" width="10" height="24"/><rect x="66" y="12" width="10" height="50"/><rect x="86" y="26" width="10" height="36"/><rect x="106" y="16" width="10" height="46"/><rect x="126" y="4" width="10" height="58"/><rect x="146" y="22" width="10" height="40" fill="var(--cyan)"/></g>
        <g font-family="Montserrat,sans-serif" font-size="3" fill="var(--muted)"><text x="6" y="68">Q1</text><text x="26" y="68">Q2</text><text x="46" y="68">Q3</text><text x="66" y="68">Q4</text><text x="86" y="68">Q5</text><text x="106" y="68">Q6</text><text x="126" y="68">Q7</text><text x="146" y="68">Q8</text></g>
      </svg>
    </div>
    <div class="slide">
      <div class="t">DASHBOARD</div><div class="num">39</div>
      <div class="box" style="left:8px;top:20px;width:38px;height:26px"></div>
      <div class="box" style="left:8px;top:50px;width:38px;height:38px"></div>
      <div class="stat" style="left:12px;top:24px;font-size:5px">82%</div><div class="p" style="left:12px;top:31px;width:32px">On time reports</div>
      <div class="stat" style="left:12px;top:54px;font-size:5px;color:var(--pink)">1.2k</div><div class="p" style="left:12px;top:61px;width:32px">New patients this month</div>
      <svg style="left:52px;top:22px" width="115" height="66" viewBox="0 0 115 66"><g stroke="var(--line)" stroke-width=".4"><line x1="0" y1="16" x2="115" y2="16"/><line x1="0" y1="36" x2="115" y2="36"/><line x1="0" y1="56" x2="115" y2="56"/></g><polyline points="0,50 18,38 36,44 54,22 72,30 90,12 115,18" fill="none" stroke="var(--cyan)" stroke-width="1.8"/><polyline points="0,60 18,52 36,56 54,42 72,48 90,36 115,38" fill="none" stroke="var(--pink)" stroke-width="1.8"/></svg>
    </div>
    <div class="slide">
      <div class="t">DASHBOARD</div><div class="num">40</div>
      <svg style="left:50px;top:20px" width="76" height="42" viewBox="0 0 76 42"><path d="M6 38a32 32 0 0 1 64 0" fill="none" stroke="var(--card-light)" stroke-width="10"/><path d="M6 38a32 32 0 0 1 50 -26" fill="none" stroke="var(--cyan)" stroke-width="10"/><text x="38" y="38" text-anchor="middle" font-size="7" font-weight="800" fill="#fff" font-family="Montserrat,sans-serif">72%</text></svg>
      <div class="box" style="left:8px;top:66px;width:159px;height:22px"></div>
      <div class="h" style="left:13px;top:70px">Machine use</div><div class="p" style="left:13px;top:76px;width:70px">Average scanner use this week.</div>
      <div class="bar" style="left:90px;top:73px;width:70px"></div><div class="bar" style="left:90px;top:73px;width:50px;background:var(--cyan)"></div>
      <div class="bar" style="left:90px;top:79px;width:70px"></div><div class="bar" style="left:90px;top:79px;width:36px;background:var(--pink)"></div>
    </div>

    <!-- Row 11 -->
    <div class="slide">
      <div class="ph" style="left:0;top:0;width:80px;height:96px;border-radius:0 48px 48px 0" role="img" aria-label="Reception photo"></div>
      <div class="brand" style="left:90px;top:16px"><span class="dot"></span>Brightwell</div>
      <div class="big" style="left:90px;top:28px">GET IN<br>TOUCH</div>
      <div class="row" style="left:90px;top:50px"><i></i>+1 555 014 2290</div>
      <div class="row" style="left:90px;top:59px"><i></i>hello@brightwellimaging.com</div>
      <div class="row" style="left:90px;top:68px"><i></i>120 Harbor Lane, Suite 4</div>
    </div>
    <div class="slide">
      <div class="t">BLANK SLIDE</div><div class="num">42</div>
    </div>
  </div>
</div>
</body>
</html>
```